Mirela Causo Photography

I need a website design for my photography business, I want something clean, elegant, Classy.. I like the colors, White, Black, Green/Blue, Pink, Brown, Lavender,, I have a lot added my Logo .... Additional Info... I need a Photography Website Design, with probably 6 Tabs, Home, About Me, Portfolio, Gallery, Investment, Contact.
Home Page should have my logo, Name & Address, Social Media Icons, and Pictures.
As long as the templates are made I have a hosting coming that will code it.
Target Market(s)
Portraits Photography, Senior Portraits, Newborn, Families, Events, Engagements, Wedding,
Industry/Entity Type
Business
Number of Pages Required
5+ page
Look and feel

```html
<!DOCTYPE html>
<html lang="en">
<head>
<meta charset="utf-8">
<title>About Me — Mirela Causo Photography</title>
<link rel="stylesheet" href="https://fonts.googleapis.com/css2?family=Rock+Salt&family=Roboto+Condensed:ital,wght@0,400;0,700;1,400;1,700&display=swap">
<style>
  :root {
    --ink: #0e0e0e;
    --teal: #2a9d8a;
    --teal-soft: rgba(42, 157, 138, 0.75);
    --paper: #ffffff;
    --panel: rgba(235, 238, 240, 0.6);
    --card: #2c2c2c;
    --brand-ink: #262626;
  }
  * { margin: 0; padding: 0; box-sizing: border-box; }
  html, body { width: 1200px; height: 750px; overflow: hidden; background: var(--ink); }
  .page { position: relative; width: 1200px; height: 750px; overflow: hidden; font-family: "Roboto Condensed", sans-serif; }

  .hero-photo {
    position: absolute; left: 0; top: 74px; width: 1200px; height: 653px;
    background:
      radial-gradient(ellipse at 30% 40%, rgba(120, 110, 100, 0.55), transparent 55%),
      linear-gradient(90deg, #8a9296 0%, #b5b9b8 45%, #8e989c 75%, #a7a9a4 100%);
  }

  .top-rule { position: absolute; left: 0; top: 0; width: 1200px; height: 4px; background: var(--teal); }
  .main-nav { position: absolute; left: 0; top: 4px; width: 1200px; height: 70px; background: var(--ink); }
  .main-nav .tab {
    position: absolute; top: 0; height: 70px; line-height: 80px;
    font-family: "Rock Salt", cursive; font-size: 26px; color: var(--paper);
    text-decoration: none; white-space: nowrap;
  }
  .main-nav .tab.is-active { background: var(--teal-soft); height: 107px; padding: 0 6px; }

  .social { position: absolute; top: 80px; right: 10px; display: flex; gap: 15px; }
  .social span { width: 30px; height: 30px; border-radius: 50%; background: #151515; display: block; }

  .brand {
    position: absolute; left: 0; top: 120px; width: 1200px;
    display: flex; justify-content: center; align-items: center; gap: 12px;
  }
  .brand-mark { width: 44px; height: 44px; border-radius: 50%; background: var(--brand-ink); }
  .brand-name { font-size: 28px; font-weight: 400; color: var(--brand-ink); line-height: 1; }

  .about-panel {
    position: absolute; left: 386px; top: 178px; width: 415px; height: 430px;
    background: var(--panel); border-radius: 8px;
  }
  .about-title {
    position: absolute; left: 28px; top: 14px; width: 360px; height: 68px;
    background: var(--ink); border-radius: 8px; color: var(--paper);
    font-size: 29px; font-weight: 700; font-style: italic; text-align: center; line-height: 68px;
  }
  .about-text {
    position: absolute; left: 29px; top: 104px; width: 360px; height: 304px;
    background: var(--card); border-radius: 8px; color: var(--paper);
    font-size: 26px; font-style: italic; line-height: 34px; padding: 8px 6px;
    overflow-wrap: anywhere; overflow: hidden;
  }

  .site-footer {
    position: absolute; left: 0; top: 727px; width: 1200px; height: 23px; background: var(--ink);
    color: var(--paper); font-size: 10px; font-weight: 700; text-align: center; line-height: 23px;
  }
</style>
</head>
<body>
<div class="page">
  <div class="hero-photo" role="img" aria-label="Soft-focus photo of a photographer holding a camera on a city street"></div>

  <div class="brand">
    <span class="brand-mark"></span>
    <span class="brand-name">Mirela Causo Photography</span>
  </div>

  <div class="top-rule"></div>
  <nav class="main-nav">
    <a class="tab" style="left:222px">Home</a>
    <a class="tab is-active" style="left:306px">About Me</a>
    <a class="tab" style="left:469px">Portfolio</a>
    <a class="tab" style="left:614px">Gallery</a>
    <a class="tab" style="left:747px">Investment</a>
    <a class="tab" style="left:919px">Contact</a>
  </nav>

  <div class="social" aria-label="Social media links">
    <span></span><span></span><span></span><span></span>
  </div>

  <section class="about-panel">
    <h1 class="about-title">Mirela Causo</h1>
    <p class="about-text">agnglabsjagsuhfaj gau;’ab/jlfa-huahbjg’haub/asfh’/iaolsbflakjshjs-fhasjh ajsbfj ash iashf hsiansfia ishf’asnf’iashf asfa hskfhasio’fh asfnkashf ‘asfas fiashjfi kans’fknaskofn ask fh’asi’of as’hfn aks nfaksnf k;afkshask/hfiasfo/as-fkasnfkasf</p>
  </section>

  <footer class="site-footer">Awesome Photography. All Rights Reserved</footer>
</div>
</body>
</html>
```